Web Design Project

I need a three page website. I have designed the index.html and the specialevent.html page.

I need someone to finetune the pages for me.

Where I have difficulty is with the following:
I want to add an event table driven by php database.
The administrator of the event will login and create the wording that fits under each colmn. The administrator the submit the form to php database. The database then display in a html.

The Table contains 5 coloums and the rows can vary and can go up to as many as 100.

The table set out events on a program
In the last column of every row I need a submit button to "View and Book" I need to link those buttons with external links/pages.

I use Dreamweaver CS5 and I need to have it in this format in order for me to edit it in the future.

The Table needs to be updated once a year for this program. So ideally if someone has a password to update the certain regions this is what I have in mind.

I have also designed a mockup of the restaurant page. At the top I need.
1) 4 Colapsable panels
a) Restaurants - opening the names of the restaurants
b) Coffee shops and light lunches .... with the names
c) Family
d) Home eateries

From the colapsable panel of each of these I need a anchored link to the description/photos of each...with a BOOK now button I can submit bookings to.

I added a colapsable panel in each restaurants description to keep everything contained.

Please help

• Background must be fixed so that main.div scroll over it

The colours are chosen so please stick to it.

The green for the submit button I short is. #C8D707

I need to edit the pages in Dreamweaver CS5. /Flexilayout2pro

Please ask if you need to know anything. I exactly know what I want.

Kind regards
Marius Delport

The colours are fine.

The wording " lindekloofdirect BOOKING agent" should appear right at the top in the white horizon part of the background image.

The specialevent page I described already. I am interested in the editable solution. for this.

I will make up a mockup of the third page and send it later.

Regards

```html
<!DOCTYPE html>
<html lang="en">
<head>
<meta charset="utf-8">
<title>lindekloofdirect – Food &amp; Drink</title>
<link href="https://fonts.googleapis.com/css2?family=Tinos:ital,wght@0,400;1,700&family=Open+Sans:wght@400;600;700&display=swap" rel="stylesheet">
<style>
:root{
  --lime:#c8d707;
  --page-grey:#666666;
  --panel:#ffffff;
  --bar:#dcdcdc;
  --bar-line:#ececec;
  --icon:#9a9a9a;
  --heading-green:#5d9a1f;
  --text:#1e1e1e;
  --rule:#8a8a8a;
  --btn-top:#c8d707;
  --btn-bottom:#7f8a05;
}
*{box-sizing:border-box;margin:0;padding:0}
html,body{width:1099px;height:1200px;overflow:hidden}
body{position:relative;background:var(--page-grey);font-family:"Open Sans",sans-serif;color:var(--text)}
.hero-backdrop{position:absolute;left:0;top:0;width:1099px;height:699px;
  background:linear-gradient(180deg,#ffffff 0%,#f4f4f2 5%,#cfcdc6 10%,#a9a69c 20%,#8d8a80 35%,#6f6d66 55%,#8c8a84 75%,#5a5955 100%)}
.brand{position:absolute;left:157px;top:6px;font-family:"Tinos",serif;font-size:31px;color:var(--lime);letter-spacing:-0.5px}
.main-nav{position:absolute;left:143px;top:168px;width:814px;height:40px;border-radius:20px;background:var(--lime);
  box-shadow:0 2px 3px rgba(0,0,0,.25);display:flex;justify-content:center;align-items:center;gap:0}
.main-nav a{font-family:"Tinos",serif;font-size:13px;color:#fff;text-decoration:none;text-shadow:0 1px 1px rgba(0,0,0,.35)}
.main-nav a.home{margin-right:34px}
.main-nav a.accom{margin-right:34px}
.main-nav a.play{margin-right:47px}
.tagline{position:absolute;left:158px;top:220px;font-family:"Tinos",serif;font-style:italic;font-weight:700;font-size:28px;color:#fff;text-shadow:0 1px 2px rgba(0,0,0,.4)}
.content-panel{position:absolute;left:143px;top:280px;width:814px;height:907px;background:var(--panel);border-radius:16px}
.page-title{position:absolute;left:12px;top:14px;width:788px;height:37px;background:var(--bar);border-radius:10px 10px 0 0;
  color:#fff;font-size:26px;line-height:37px;padding-left:14px}
.accordion{position:absolute;left:12px;top:72px;width:788px}
.acc-head{height:38px;background:var(--bar);border-bottom:2px solid var(--bar-line);color:#fff;font-size:17px;line-height:38px;padding-left:12px;position:relative}
.acc-head svg{position:absolute;right:16px;top:11px}
.acc-body{border:3px solid var(--bar);border-top:none;background:#fff;height:172px;padding:5px 10px 0 9px;font-size:11.6px;line-height:15px;letter-spacing:.2px}
.acc-body p{margin-bottom:18px}
.acc-body address{font-style:normal;line-height:17px}
.listing{position:absolute;left:14px;width:788px}
.listing h2{font-size:20px;font-weight:700;color:var(--heading-green);height:27px}
.listing hr{border:none;border-top:1px solid var(--rule);margin-top:2px}
.thumbs{position:absolute;left:1px;top:44px;display:grid;grid-template-columns:repeat(3,93px);grid-auto-rows:61px;column-gap:12px;row-gap:11px}
.thumb.meadow{background:linear-gradient(180deg,#7fa6d4 0%,#c5d6e6 30%,#6f7f5e 45%,#c9c73a 60%,#b4bd2c 100%)}
.thumb.bridge{background:linear-gradient(180deg,#56603d 0%,#7e7a56 35%,#a39a86 55%,#6c6355 75%,#8a8070 100%)}
.listing .blurb{position:absolute;left:323px;top:45px;width:430px;font-size:11.6px;line-height:14.6px;letter-spacing:.2px}
.book-btn{position:absolute;left:683px;top:142px;width:98px;height:27px;border-radius:4px;border:1px solid #6e7804;
  background:linear-gradient(180deg,var(--btn-top),var(--btn-bottom));color:#1a1a1a;font-family:"Open Sans",sans-serif;font-size:14px;text-align:center;line-height:25px}
</style>
</head>
<body>
<div class="hero-backdrop" role="img" aria-label="Sepia photograph of a Karoo valley town with mountains and a winding road"></div>
<div class="brand">lindekloofdirect</div>
<nav class="main-nav">
  <a class="home" href="#">Home</a>
  <a class="accom" href="#">Accommodation</a>
  <a class="play" href="#">Play</a>
  <a href="#">Contact</a>
</nav>
<div class="tagline">Your booking agent for</div>

<main class="content-panel">
  <h1 class="page-title" style="font-weight:400">Food &amp; Drink</h1>
  <section class="accordion">
    <div class="acc-head">Restaurants<svg width="18" height="4"><rect width="18" height="4" fill="var(--icon)"/></svg></div>
    <div class="acc-head">Coffe shops and Lunch<svg width="18" height="18" style="top:10px"><rect y="7" width="18" height="4" fill="var(--icon)"/><rect x="7" width="4" height="18" fill="var(--icon)"/></svg></div>
    <div class="acc-body">
      <p>Lorem Ipsum is simply dummy text of the printing and typesetting industry. Lorem Ipsum has been the industry's standard dummy text ever since the 1500s, when an unknown printer took a galley of type and scrambled it to make a type specimen book. It has survived not only five centuries, but also the leap into electronic typesetting, remaining essentially unchanged. It was popularised in the 1960s with the release of Letraset sheets containing. but also the leap into electronic typesetting, remaining essentially unchanged. It was popularised in the 1960s with the release of Letraset sheets.</p>
      <address>South Africa - Western Cape,<br>14 Kerk Street,<br>Lindekloof, 6930<br>Email: bookings@lindekloofdirect.co.za</address>
    </div>
    <div class="acc-head" style="margin-top:4px">Home Eateries<svg width="18" height="4"><rect width="18" height="4" fill="var(--icon)"/></svg></div>
    <div class="acc-head">Family Steakhouse<svg width="18" height="4"><rect width="18" height="4" fill="var(--icon)"/></svg></div>
    <div class="acc-head">Take aways<svg width="18" height="4"><rect width="18" height="4" fill="var(--icon)"/></svg></div>
  </section>

  <article class="listing" style="top:494px">
    <h2>Karoo Hearth</h2><hr>
    <div class="thumbs">
      <div class="thumb meadow" role="img" aria-label="Meadow under mountains"></div>
      <div class="thumb bridge" role="img" aria-label="Stone bridge among trees"></div>
      <div class="thumb bridge" role="img" aria-label="Stone bridge among trees"></div>
      <div class="thumb meadow" role="img" aria-label="Meadow under mountains"></div>
      <div class="thumb bridge" role="img" aria-label="Stone bridge among trees"></div>
      <div class="thumb bridge" role="img" aria-label="Stone bridge among trees"></div>
    </div>
    <p class="blurb">Lorem Ipsum is simply dummy text of the printing and typesetting industry. Lorem Ipsum has been the industry's standard dummy text ever since the 1500s, when an unknown printer took a galley of type and scrambled it to make a type specimen book. It has survived not only five centuries, but also the leap into electronic typesetting, remaining essentially unchanged. It was popularised in the 1960s with the release of Letraset sheets containing.</p>
    <a class="book-btn" href="#" style="text-decoration:none">Read More</a>
  </article>

  <article class="listing" style="top:706px">
    <h2>Karoo Hearth</h2><hr>
    <div class="thumbs">
      <div class="thumb meadow" role="img" aria-label="Meadow under mountains"></div>
      <div class="thumb bridge" role="img" aria-label="Stone bridge among trees"></div>
      <div class="thumb bridge" role="img" aria-label="Stone bridge among trees"></div>
      <div class="thumb meadow" role="img" aria-label="Meadow under mountains"></div>
      <div class="thumb bridge" role="img" aria-label="Stone bridge among trees"></div>
      <div class="thumb bridge" role="img" aria-label="Stone bridge among trees"></div>
    </div>
    <p class="blurb">Lorem Ipsum is simply dummy text of the printing and typesetting industry. Lorem Ipsum has been the industry's standard dummy text ever since the 1500s, when an unknown printer took a galley of type and scrambled it to make a type specimen book. It has survived not only five centuries, but also the leap into electronic typesetting, remaining essentially unchanged. It was popularised in the 1960s with the release of Letraset sheets containing.</p>
    <a class="book-btn" href="#" style="text-decoration:none">Read More</a>
  </article>
</main>
</body>
</html>
```